Single Page Production Company Site

Clean. Simple. Minimalist site with one page.

No portfolio, just some text to communicate a general overview of what the company does.

We work for a very select group of clients, creating strong brand personalities online. The site is specifically minimal and not communicating too much about what we do.. we have a variety of capabilities to work with clients and prefer to be broad with just a simple landing page as the point of contact for our brand.
Updates

Christmas holidays are coming up, maybe people need some time away from work with family and friends... We can keep working on this and I will provide feedback as quickly as possible, but I understand if designers have other commitments during the coming days. Thanks for your hard work!

Industry/Entity Type

Design Agency

Coding

Coded - Design and coding required

Number of Pages Required

1 page

Font styles to use
Sans Serif

Requirements
Must have
• Clean, bold text headlines.
Nice to have
• Unsure about any images used in the design, would like to see options with or without.

```html
<!DOCTYPE html>
<html lang="en">
<head>
<meta charset="utf-8">
<title>Crestline Studio</title>
<link href="https://fonts.googleapis.com/css2?family=Poppins:wght@400;500;600;700&family=Roboto:wght@300;400;500&display=swap" rel="stylesheet">
<style>
:root{
  --orange:#ff4a17;
  --orange-2:#ff7a3d;
  --navy:#161733;
  --text:#2a2a2a;
  --muted:#8a8a8a;
  --light:#f6f6f6;
  --line:#e4e4e4;
  --white:#fff;
}
*{box-sizing:border-box;margin:0;padding:0}
html,body{width:1200px;height:3141px;overflow:hidden}
body{font-family:'Roboto',sans-serif;color:var(--text);background:var(--white);position:relative}
.h{font-family:'Poppins',sans-serif}
section,header,footer{position:absolute;left:0;width:1200px}
.abs{position:absolute}

/* header */
.site-header{top:0;height:84px;background:var(--white);box-shadow:0 2px 8px rgba(0,0,0,.05);z-index:2}
.brand{left:163px;top:26px;display:flex;align-items:center;gap:10px}
.brand-dot{width:30px;height:30px;border-radius:50%;background:var(--orange)}
.brand-name{font-family:'Poppins',sans-serif;font-weight:600;font-size:17px;color:var(--navy)}
.nav{left:544px;top:34px;font-family:'Poppins',sans-serif;font-size:11px;font-weight:500;color:var(--navy)}
.nav a{position:absolute;white-space:nowrap;text-decoration:none;color:inherit}
.nav a.active{color:var(--orange)}
.nav-marker{left:559px;top:50px;width:2px;height:34px;background:var(--orange)}
.login-btn{left:896px;top:29px;width:143px;height:25px;border:1.5px solid var(--orange);border-radius:14px;font-size:10.5px;color:var(--orange);display:flex;align-items:center;justify-content:center;font-family:'Poppins',sans-serif}

/* hero */
.hero{top:84px;height:517px;background:#f1f1f1}
.hero-title{left:163px;top:150px;width:520px;font-weight:700;font-size:37px;line-height:41px;color:var(--navy)}
.hero-text{left:163px;top:290px;width:500px;padding-left:12px;border-left:3px solid var(--orange);font-size:13px;line-height:19px;color:#666}
.hero-art{left:680px;top:160px;width:360px;height:200px;border-radius:6px;background:linear-gradient(135deg,#dfe3ef,#f4d98a 55%,#cfd6ea)}

/* process */
.process{top:601px;height:513px;text-align:center}
.eyebrow{font-family:'Poppins',sans-serif;font-size:12px;font-weight:500;color:#777;letter-spacing:.5px}
.process .eyebrow{position:absolute;top:56px;width:100%}
.section-title{font-family:'Poppins',sans-serif;font-weight:500;font-size:27px;color:var(--navy)}
.process .section-title{position:absolute;top:75px;width:100%}
.step-card{top:157px;width:277px;height:281px;background:var(--white);box-shadow:0 2px 12px rgba(0,0,0,.08);text-align:left;padding:58px 22px 0 22px}
.step-card svg{display:block;margin-bottom:10px}
.step-title{font-family:'Poppins',sans-serif;font-weight:500;font-size:16px;color:var(--navy);margin-bottom:10px}
.step-text{font-size:11px;line-height:18px;color:#888;text-align:justify}

/* team */
.team{top:1114px;height:300px}
.team-photo{left:0;top:0;width:438px;height:295px;background:linear-gradient(120deg,#3b3b44,#9aa2ad 60%,#d9dde2)}
.team-copy{left:536px;top:0;width:500px}
.label{font-family:'Poppins',sans-serif;font-weight:500;font-size:12px;color:#888;letter-spacing:.4px;margin-bottom:10px}
.lead{font-size:12.5px;line-height:21px;color:var(--navy);font-weight:500}
.sub-title{font-family:'Poppins',sans-serif;font-weight:500;font-size:16px;color:var(--navy);margin:26px 0 12px;display:flex;align-items:center;gap:8px}
.sub-title::before{content:"";width:0;height:0;border-left:7px solid var(--orange);border-top:6px solid transparent;border-bottom:6px solid transparent}
.body-text{font-size:11px;line-height:20px;color:#8d8d8d}

/* goal */
.goal{top:1470px;height:330px}
.goal-copy{left:161px;top:10px;width:510px}
.goal-photo{left:760px;top:19px;width:440px;height:295px;background:linear-gradient(135deg,#5c5248,#b39a80 50%,#e3ded7)}

/* we get you */
.promise{top:1859px;height:348px;background:var(--light)}
.promise-card{left:161px;top:61px;width:876px;height:168px;background:var(--white);box-shadow:0 2px 10px rgba(0,0,0,.06);text-align:center;padding:42px 70px 0}
.promise-title{font-family:'Poppins',sans-serif;font-weight:600;font-size:16px;color:var(--navy);display:flex;align-items:center;justify-content:center;gap:12px;margin-bottom:14px}
.promise-title::before,.promise-title::after{content:"";width:24px;height:2px;background:var(--orange)}
.promise-card .body-text{font-size:10.5px;line-height:20px}
.promise-card .tagline{color:var(--navy);font-style:italic;margin-top:6px;font-size:10.5px}

/* contact */
.contact{top:2207px;height:446px;text-align:center}
.contact .eyebrow{position:absolute;top:76px;width:100%}
.contact .section-title{position:absolute;top:98px;width:100%}
.field{position:absolute;height:30px;border:1px solid var(--line);border-radius:3px;font-size:10px;color:#999;text-align:left;padding:8px 10px}
.send-btn{left:547px;top:339px;width:106px;height:28px;border-radius:14px;background:linear-gradient(90deg,var(--orange),var(--orange-2));color:var(--white);font-family:'Poppins',sans-serif;font-weight:600;font-size:10px;display:flex;align-items:center;justify-content:center;gap:6px;box-shadow:0 4px 10px rgba(255,74,23,.3)}

/* footer */
.site-footer{top:2653px;height:438px;background:var(--light)}
.call-title{top:60px;width:100%;text-align:center;font-family:'Poppins',sans-serif;font-size:16px;color:var(--navy)}
.contact-item{top:104px;display:flex;align-items:center;gap:12px;font-size:11px;color:#666}
.icon-box{width:26px;height:26px;border:1px solid #ddd;display:flex;align-items:center;justify-content:center;background:var(--white)}
.rule{left:161px;top:157px;width:876px;height:1px;background:var(--line)}
.col-title{font-family:'Poppins',sans-serif;font-weight:600;font-size:13px;color:var(--navy);margin-bottom:16px}
.links{list-style:none;font-size:11px;line-height:26px;color:#777}
.foot-about{left:161px;top:196px;width:280px}
.foot-about .body-text{margin-top:22px;font-size:11px;color:#777}
.foot-about .more{color:var(--navy);font-weight:500}
.socials{display:flex;gap:15px;margin-top:16px;align-items:center}
.social-link{width:11px;height:11px;border-radius:2px;background:#6f6f78}
.social-link.is-first{background:var(--orange)}
.email-field{margin-top:14px;width:202px;height:30px;border:1px solid #ddd;border-radius:15px;background:var(--white);font-size:10px;color:#999;display:flex;align-items:center;padding-left:12px;gap:6px}
.subscribe{margin-top:10px;width:202px;height:32px;border-radius:16px;background:linear-gradient(90deg,var(--orange),var(--orange-2));color:var(--white);font-family:'Poppins',sans-serif;font-weight:600;font-size:11px;display:flex;align-items:center;justify-content:center}
.bottom-bar{top:3091px;height:50px;background:var(--white);border-top:1px solid var(--line);text-align:center;font-size:10.5px;color:#777;line-height:50px}
</style>
</head>
<body>

<header class="site-header">
  <div class="brand abs"><span class="brand-dot"></span><span class="brand-name">Crestline Studio</span></div>
  <nav class="nav abs">
    <a class="active" style="left:0">HOME</a>
    <a style="left:63px">SERVICES</a>
    <a style="left:145px">ABOUT</a>
    <a style="left:212px">BLOG</a>
    <a style="left:271px">CONTACT</a>
  </nav>
  <div class="nav-marker abs"></div>
  <div class="login-btn abs">Login - OR - Register</div>
</header>

<section class="hero">
  <h1 class="hero-title h abs">WE CREATE THE PERFECT ONLINE PRESENCE FOR YOUR BRAND.</h1>
  <p class="hero-text abs">We do it all when it comes to online commerce for retail stores, wholesalers and distributors. Taking your company online introduces a world of</p>
  <div class="hero-art abs" role="img" aria-label="Flat illustration of a web workspace with a monitor, tools and media icons"></div>
</section>

<section class="process">
  <p class="eyebrow">OUR WORKING PROCESS</p>
  <h2 class="section-title">We’re Custom Website Design and Development Experts</h2>

  <article class="step-card abs" style="left:161px">
    <svg width="44" height="40" viewBox="0 0 44 40"><circle cx="18" cy="15" r="7" fill="#161733"/><path d="M4 38c0-9 6-14 14-14s14 5 14 14z" fill="#161733"/><rect x="26" y="2" width="16" height="10" rx="3" fill="#ff4a17"/></svg>
    <h3 class="step-title">1. Concept</h3>
    <p class="step-text">We are leading the way in design innovation for modern websites. Clean, functional, intuitive websites for progressive businesses.</p>
  </article>
  <article class="step-card abs" style="left:461px">
    <svg width="44" height="40" viewBox="0 0 44 40"><rect x="3" y="4" width="38" height="26" rx="2" fill="none" stroke="#161733" stroke-width="3"/><path d="M10 23l8-8 6 5 9-10" fill="none" stroke="#ff4a17" stroke-width="3"/><rect x="17" y="32" width="10" height="5" fill="#161733"/></svg>
    <h3 class="step-title">2. Create</h3>
    <p class="step-text">Building brands through design, we believe that contrast is everything. For industry leaders who set the pace and exceed expectations, we help give the company voice and soul.</p>
  </article>
  <article class="step-card abs" style="left:760px">
    <svg width="44" height="40" viewBox="0 0 44 40"><rect x="3" y="4" width="32" height="26" rx="2" fill="none" stroke="#161733" stroke-width="3"/><line x1="3" y1="11" x2="35" y2="11" stroke="#161733" stroke-width="3"/><path d="M13 16l-4 4 4 4M25 16l4 4-4 4" fill="none" stroke="#161733" stroke-width="2"/><circle cx="36" cy="31" r="6" fill="#ff4a17"/></svg>
    <h3 class="step-title">3. Complete</h3>
    <p class="step-text">Clients look to us for unique, exceptional solutions to their technology issues. We bring creativity to the table and solve your business’ problems with actionable solutions.</p>
  </article>
</section>

<section class="team">
  <div class="team-photo abs" role="img" aria-label="Photo of team members working at desktop computers"></div>
  <div class="team-copy abs">
    <p class="label">THE STUDIO TEAM</p>
    <p class="lead">Crestline Studio focuses on creating extraordinary online experiences for extraordinary clients. We’ll work with you to create the perfect online presence for your brand.</p>
    <h3 class="sub-title">Size is Everything.</h3>
    <p class="body-text">We don’t work in a massive corporate office and we don’t have a mailroom. Not that there’s anything wrong with that, it’s just that we like knowing each other’s names, and encourage our clients to know ours. Our small staff has an advantage – our group works more efficiently, more cost-effectively and most importantly, flexible to each client’s unique needs. We deliver a range of services found at any agency, with the personal service you should expect.</p>
  </div>
</section>

<section class="goal">
  <div class="goal-copy abs">
    <p class="label">OUR GOAL.</p>
    <p class="body-text">Crestline Studio brings your brand to life, online. We do it all when it comes to online commerce for retail stores, wholesalers and distributors. Taking your company online introduces a world of opportunity, as well as specific challenges associated with online trade. We’ll assist you in establishing a successful online presence and bringing your brand to a worldwide audience.</p>
    <h3 class="sub-title" style="margin-top:12px">Who’s Owen?</h3>
    <p class="body-text">Owen Marlow, owner of Crestline Studio is not your typical principal. He’s worked internationally with both Halden Media and Northgate Press publications in photo production for titles including Parlour and Lantern Weekly. Originally from coastal Maine and an all-around New Englander, Owen can often be found sailing during the summer and skiing during winter. He believes that inspiration comes from experiencing the world, not from sitting in a cubicle. But no worries, his biggest fear is being offline, and is always within an arms reach of the Internet.</p>
  </div>
  <div class="goal-photo abs" role="img" aria-label="Photo of a team joining hands over a table with laptops"></div>
</section>

<section class="promise">
  <div class="promise-card abs">
    <h2 class="promise-title">We Get You.</h2>
    <p class="body-text">Having a website isn’t enough. You need to show your customers you understand the socially connected online world we live in. We help you create designs that capture the personality of your business and project the image you want your customers to see. Maybe you’re a small company looking to sell yourself in the big leagues, maybe you’re a big company that wants to look approachable; either way, we can make it happen.</p>
    <p class="tagline">You’ll come across looking professional, unique and strikingly hip all at the same time.</p>
  </div>
</section>

<section class="contact">
  <p class="eyebrow">LET’S TALK</p>
  <h2 class="section-title">Get In Touch</h2>
  <div class="field" style="left:237px;top:161px;width:357px">First Name</div>
  <div class="field" style="left:605px;top:161px;width:358px">Last Name</div>
  <div class="field" style="left:237px;top:203px;width:357px">Email</div>
  <div class="field" style="left:605px;top:203px;width:358px">Phone</div>
  <div class="field" style="left:237px;top:243px;width:726px;height:80px">Message</div>
  <div class="send-btn abs">SEND
    <svg width="10" height="10" viewBox="0 0 10 10"><path d="M0 5L10 0 7 10 5 6z" fill="#fff"/></svg>
  </div>
</section>

<footer class="site-footer">
  <p class="call-title abs">Any Queries? Don’t Hesitate? Feel Free to Make a Call</p>
  <div class="contact-item abs" style="left:410px">
    <span class="icon-box"><svg width="12" height="9" viewBox="0 0 12 9"><rect x=".5" y=".5" width="11" height="8" fill="none" stroke="#555"/><path d="M.5 .5L6 5l5.5-4.5" fill="none" stroke="#555"/></svg></span>hello@crestlinestudio.com
  </div>
  <div class="contact-item abs" style="left:642px">
    <span class="icon-box"><svg width="11" height="11" viewBox="0 0 12 12"><path d="M2 1l2.5 0 1 3-1.5 1c.7 1.5 1.8 2.6 3 3l1-1.5 3 1V10c0 .6-.5 1-1 1C5 11 1 7 1 2c0-.5.4-1 1-1z" fill="#555"/></svg></span>+1 - 555 - 0142 - 7788
  </div>
  <div class="rule abs"></div>

  <div class="foot-about abs">
    <div class="brand" style="display:flex;align-items:center;gap:10px"><span class="brand-dot"></span><span class="brand-name">Crestline Studio</span></div>
    <p class="body-text">We help you create designs that capture the personality of your business and project the image you want your customers to see. Maybe you’re a small company looking to sell yourself in the … <span class="more">continue reading</span></p>
    <div class="socials" aria-label="Social links">
      <span class="social-link is-first"></span><span class="social-link"></span><span class="social-link"></span><span class="social-link"></span><span class="social-link"></span><span class="social-link"></span><span class="social-link"></span>
    </div>
  </div>
  <div class="abs" style="left:461px;top:200px">
    <h4 class="col-title">OUR SERVICES</h4>
    <ul class="links"><li>Custom Web Design &amp; Development</li><li>Search Engine Optimization</li><li>Marketing</li><li>Ecommerce Development</li><li>Content Strategy</li></ul>
  </div>
  <div class="abs" style="left:685px;top:200px">
    <h4 class="col-title">QUICK LINKS</h4>
    <ul class="links"><li>Home</li><li>Services</li><li>About</li><li>Blog</li><li>Contact</li></ul>
  </div>
  <div class="abs" style="left:836px;top:200px;width:210px">
    <h4 class="col-title">NEWSLETTER</h4>
    <p class="body-text" style="font-size:11px;line-height:17px;color:#777">Subscribe to our Newsletter to get latest news and updates regarding design.</p>
    <div class="email-field"><svg width="10" height="8" viewBox="0 0 12 9"><rect x=".5" y=".5" width="11" height="8" fill="none" stroke="#999"/><path d="M.5 .5L6 5l5.5-4.5" fill="none" stroke="#999"/></svg>Your email Address</div>
    <div class="subscribe">Subscribe</div>
  </div>
</footer>

<div class="bottom-bar abs" style="left:0;width:1200px">© 2018 Crestline Studio | All rights reserved.</div>

</body>
</html>
```